Business Card Design for a Lending Business (Hard Money loans)

We need a business card for our Real Estate Lending business. We do hard Money loans for real estate investors. We have an existing logo we like, see attached. I'd like the business card to mostly include the logo colors, but a bright color pop of some sort would be nice to see also. Card should include Logo, Company Name, Company Address, Employee Name, Cell Phone, Main Phone, Email, Website

Industry/Entity Type

Finance / Lending

Contact Information for Business Card

Logo, Company Name, Company Address, Employee Name, Cell Phone, Main Phone, Email, Website

Requirements
Nice to have
• I'd like the business card to mostly include the logo colors, but a bright color pop of some sort would be nice to see also.

```html
<!DOCTYPE html>
<html lang="en">
<head>
<meta charset="utf-8">
<title>Keystone Lending – Business Card</title>
<link rel="stylesheet" href="https://fonts.googleapis.com/css2?family=Lato:wght@400;700;900&display=swap">
<style>
  :root {
    --stage: #2b2d31;
    --navy: #1f2f86;
    --navy-deep: #1b2878;
    --royal: #263b8e;
    --cyan: #1ba3df;
    --white: #ffffff;
    --ink-grey: #5b5f66;
    --faint: #f0f1f3;
  }
  * { box-sizing: border-box; margin: 0; padding: 0; }
  html, body {
    width: 1200px; height: 952px; overflow: hidden;
    background: var(--stage);
    font-family: "Lato", sans-serif;
  }
  .stage {
    width: 1200px; height: 952px;
    display: flex; align-items: center; justify-content: center; gap: 60px;
  }
  .card {
    position: relative;
    width: 540px; height: 309px;
    border-radius: 22px;
    overflow: hidden;
    box-shadow: 0 14px 30px rgba(0,0,0,.35);
  }

  /* Back side */
  .card-back { background: var(--royal); }
  .card-back .faint-mark {
    position: absolute; left: -70px; top: -90px;
    width: 300px; height: 300px; border-radius: 50%;
    border: 34px solid var(--navy-deep);
    opacity: .55;
  }
  .card-back .brand-name {
    position: absolute; left: 0; right: 0; top: 50%;
    transform: translateY(-50%);
    text-align: center;
    color: var(--white);
    font-weight: 900; font-size: 40px; letter-spacing: 6px;
    text-transform: uppercase;
  }

  /* Front side */
  .card-front { background: var(--white); }
  .card-front .faint-mark {
    position: absolute; right: -40px; bottom: -120px;
    width: 300px; height: 300px; border-radius: 50%;
    border: 40px solid var(--faint);
  }
  .brand-lockup {
    position: absolute; left: 34px; top: 34px;
    display: flex; align-items: center; gap: 10px;
  }
  .brand-lockup .dot {
    width: 26px; height: 26px; border-radius: 50%;
    background: var(--cyan);
  }
  .brand-lockup .brand-name {
    color: var(--navy);
    font-weight: 900; font-size: 22px; letter-spacing: 3px;
    text-transform: uppercase;
  }
  .person {
    position: absolute; left: 34px; top: 104px;
  }
  .person .name {
    font-weight: 900; font-size: 21px; letter-spacing: .5px;
    text-transform: uppercase; color: var(--navy);
  }
  .person .name .surname { color: var(--cyan); }
  .person .role {
    font-size: 13px; color: var(--ink-grey); margin-top: 2px;
  }
  .contacts {
    position: absolute; left: 34px; top: 178px;
    list-style: none;
  }
  .contacts li {
    display: flex; align-items: center; gap: 9px;
    font-size: 13px; color: var(--ink-grey);
    margin-bottom: 9px;
  }
  .contacts .icon {
    width: 16px; height: 16px; border-radius: 3px;
    background: var(--cyan);
    display: flex; align-items: center; justify-content: center;
  }
  .office {
    position: absolute; right: 32px; top: 80px;
    text-align: right;
  }
  .office .company {
    font-weight: 900; font-size: 16px; color: var(--navy);
    text-transform: uppercase; letter-spacing: .5px;
  }
  .office .address {
    font-size: 13px; color: var(--ink-grey); line-height: 1.45; margin-top: 6px;
  }
</style>
</head>
<body>
<main class="stage">

  <section class="card card-back" aria-label="Card back">
    <div class="faint-mark"></div>
    <div class="brand-name">Keystone Lending</div>
  </section>

  <section class="card card-front" aria-label="Card front">
    <div class="faint-mark"></div>

    <div class="brand-lockup">
      <span class="dot"></span>
      <span class="brand-name">Keystone Lending</span>
    </div>

    <div class="person">
      <div class="name">Daniel R. <span class="surname">Whitford</span></div>
      <div class="role">Managing Director</div>
    </div>

    <ul class="contacts">
      <li>
        <span class="icon">
          <svg width="10" height="10" viewBox="0 0 10 10"><path d="M2 1 L4 1 L4.6 3 L3.5 3.8 Q4.5 5.8 6.2 6.5 L7 5.4 L9 6 L9 8 Q9 9 8 9 Q1 8.5 1 2 Q1 1 2 1Z" fill="#fff"/></svg>
        </span>
        +00 123 456 78
      </li>
      <li>
        <span class="icon">
          <svg width="10" height="8" viewBox="0 0 10 8"><rect x=".5" y=".5" width="9" height="7" fill="none" stroke="#fff"/><path d="M.5 .5 L5 4.5 L9.5 .5" fill="none" stroke="#fff"/></svg>
        </span>
        hello@keystonelending.com
      </li>
      <li>
        <span class="icon">
          <svg width="10" height="10" viewBox="0 0 10 10"><path d="M1 1 L9 5 L5.5 5.8 L4.5 9 Z" fill="#fff"/></svg>
        </span>
        www.keystonelending.com
      </li>
    </ul>

    <div class="office">
      <div class="company">Keystone Lending Ltd</div>
      <div class="address">1720 Meridian Avenue<br>Arlington, VA 22201</div>
    </div>
  </section>

</main>
</body>
</html>
```